Plumbing company needs Business Card Design

Hi I need business card design based on logo which I uploaded. Its plumbing and heating company called Wodorex Usługi Hydrauliczno-Gazowe. I want to see on my card motto of my company which is "...od wymiany uszczelki po wymiane łazienki.", my phone number, name, and website: 608472915, Marek Kowalczyk, info@wodorex-example.org, www.wodorex-example.org
I want to see logos of companys which I'm approved installer (Termovo) (Le Varnoux) (Kelm) (Ostra).
I want new creative look of business card. I like rounded corners.
Any questions please send message.
Thanks for intrest.
Industry/Entity Type
Business
Contact Information for Business Card
Marek Kowalczyk
608 472 915
info@wodorex-example.org
www.wodorex-example.org
...od wymiany uszczelki po wymiane łazienki.

```html
<!DOCTYPE html>
<html lang="pl">
<head>
<meta charset="utf-8">
<title>Wodorex – wizytówka</title>
<link rel="stylesheet" href="https://fonts.googleapis.com/css2?family=Cinzel:wght@400;700&family=Questrial&display=swap">
<style>
  :root {
    --navy: #213c7a;
    --red: #e3262b;
    --yellow: #f4ea1a;
    --paper: #ffffff;
    --ink-grey: #4a4a4a;
    --card-edge: #b9b9b9;
    --badge: #e9edf6;
    --soft-text: #c9d1e6;
  }
  * { margin: 0; padding: 0; box-sizing: border-box; }
  html, body { width: 1200px; height: 1200px; overflow: hidden; background: var(--paper); }
  .sheet { position: relative; width: 1200px; height: 1200px; }

  .card {
    position: absolute;
    left: 318px;
    width: 552px;
    height: 310px;
    overflow: hidden;
    border-radius: 16px;
  }
  .card--front { top: 224px; background: var(--paper); border: 1px solid var(--card-edge); }
  .card--back { top: 680px; background: var(--navy); }

  /* brand lockup */
  .brand { position: absolute; display: flex; align-items: center; gap: 8px; }
  .brand__mark {
    width: 66px; height: 66px;
    background: var(--yellow);
    border-radius: 6px;
    flex: none;
  }
  .brand__text { font-family: "Cinzel", serif; font-weight: 700; color: var(--red); line-height: 1; }
  .brand__name { font-size: 34px; letter-spacing: 0.5px; }
  .brand__trade { font-size: 12.5px; margin-top: 6px; letter-spacing: 0.2px; }

  .card--front .brand { left: 35px; top: 37px; }

  .motto {
    position: absolute;
    left: 35px; top: 150px;
    width: 215px;
    font-family: "Cinzel", serif;
    font-size: 12px;
    line-height: 1.5;
    color: var(--navy);
  }

  .contact {
    position: absolute;
    left: 277px; top: 142px;
    padding-left: 20px;
    border-left: 3px solid var(--navy);
    height: 117px;
  }
  .contact__name {
    font-family: "Cinzel", serif;
    font-size: 21px;
    font-weight: 700;
    color: var(--navy);
    letter-spacing: 0.5px;
    margin-top: 6px;
    margin-bottom: 20px;
  }
  .contact__row {
    display: flex; align-items: center; gap: 7px;
    height: 23px;
    font-family: "Cinzel", serif;
    font-size: 11px;
    color: var(--ink-grey);
  }
  .contact__tag {
    width: 15px; height: 15px;
    background: var(--red);
    color: var(--paper);
    font-family: "Cinzel", serif;
    font-size: 10px;
    font-weight: 700;
    display: flex; align-items: center; justify-content: center;
    flex: none;
  }
  .card__rule {
    position: absolute; left: 0; right: 0; top: 274px;
    height: 8px; background: var(--navy);
  }

  .partners {
    position: absolute; left: 0; right: 0; top: 20px;
    display: flex; justify-content: center; gap: 18px;
  }
  .partners__badge {
    width: 96px; height: 34px;
    background: var(--badge);
    border-radius: 5px;
  }

  .band {
    position: absolute; left: 0; right: 0; top: 73px;
    height: 81px; background: var(--paper);
    border-bottom: 8px solid var(--yellow);
    box-sizing: content-box;
  }
  .card--back .brand { left: 50%; top: 78px; transform: translateX(-50%); }
  .card--back .brand__mark { width: 70px; height: 70px; }

  .card--back .motto {
    left: 0; right: 0; top: 200px; width: auto;
    text-align: center;
    font-size: 14px;
    color: var(--paper);
  }
  .site {
    position: absolute; left: 0; right: 0; top: 274px;
    text-align: center;
    font-family: "Questrial", sans-serif;
    font-size: 12px;
    letter-spacing: 6px;
    color: var(--soft-text);
  }
</style>
</head>
<body>
<main class="sheet">
  <section class="card card--front" aria-label="Przód wizytówki">
    <div class="brand">
      <div class="brand__mark"></div>
      <div class="brand__text">
        <div class="brand__name">Wodorex</div>
        <div class="brand__trade">Usługi Hydrauliczno-Gazowe</div>
      </div>
    </div>
    <div class="contact">
      <h1 class="contact__name">Marek Kowalczyk</h1>
      <div class="contact__row"><span class="contact__tag">P</span>608 472 915</div>
      <div class="contact__row"><span class="contact__tag">E</span>info@wodorex-example.org</div>
      <div class="contact__row"><span class="contact__tag">W</span>www.wodorex-example.org</div>
    </div>
    <div class="card__rule"></div>
  </section>

  <section class="card card--back" aria-label="Tył wizytówki">
    <div class="partners">
      <div class="partners__badge" role="img" aria-label="Autoryzowany instalator: Termovo"></div>
      <div class="partners__badge" role="img" aria-label="Autoryzowany instalator: Le Varnoux"></div>
      <div class="partners__badge" role="img" aria-label="Autoryzowany instalator: Kelm"></div>
      <div class="partners__badge" role="img" aria-label="Autoryzowany instalator: Ostra"></div>
    </div>
    <div class="band"></div>
    <div class="brand">
      <div class="brand__mark"></div>
      <div class="brand__text">
        <div class="brand__name">Wodorex</div>
        <div class="brand__trade">Usługi Hydrauliczno-Gazowe</div>
      </div>
    </div>
    <p class="motto">...od wymiany uszczelki po wymianę łazienki.</p>
    <div class="site">www.wodorex-example.org</div>
  </section>
</main>
</body>
</html>
```